handmade items - handpainted and vinyl signs, hoodies, wood burned products (sold mostly at craft sales)
custom work available
home decor

Target Market(s)

woman - moms

Industry/Entity Type

craft shows

Logo Text

Pine Hollow Makers - Jenna Marsh & Brenda Okafor (with phone numbers)

Logo styles of interest
Emblem Logo
Pictorial/Combination Logo
Abstract Logo
Font styles to use
Decorative
Script

Requirements
Must have
• grain elevator
Nice to have
• train tracks

```html
<!DOCTYPE html>
<html lang="en">
<head>
<meta charset="utf-8">
<title>Pine Hollow Makers – Business Card</title>
<link href="https://fonts.googleapis.com/css2?family=Poppins:wght@300;400;500;600;700&display=swap" rel="stylesheet">
<style>
  :root {
    --page-bg: #f6f6f6;
    --card-top: #363636;
    --card-bottom: #000000;
    --ink-light: #ffffff;
    --ink-dark: #1c1c1c;
    --band-edge: #cfcfcf;
    --band-mid: #f2f2f2;
    --photo-sky: #dcdcdc;
    --photo-wall: #5a5a5a;
    --photo-ground: #3c3c3c;
  }
  * { margin: 0; padding: 0; box-sizing: border-box; }
  html, body {
    width: 1200px; height: 1200px; overflow: hidden;
    background: var(--page-bg);
    font-family: "Poppins", sans-serif;
  }
  .card {
    position: absolute; top: 172px;
    width: 513px; height: 855px; overflow: hidden;
  }
  .card-front {
    left: 60px;
    background: linear-gradient(180deg, var(--card-top) 0%, #1a1a1a 45%, var(--card-bottom) 100%);
    color: var(--ink-light);
  }
  .card-back {
    left: 631px;
    background: linear-gradient(160deg, var(--photo-wall) 0%, #8c8c8c 28%, var(--photo-sky) 45%, #b8b8b8 66%, var(--photo-ground) 100%);
  }
  .brand-name {
    position: absolute; left: 96px; top: 72px; width: 324px; height: 136px;
    display: flex; align-items: center; justify-content: center;
    text-align: center; font-weight: 600; font-size: 46px; line-height: 54px;
    letter-spacing: -0.5px;
  }
  .offer-list { position: absolute; left: 85px; top: 248px; list-style: none; }
  .offer-list li {
    position: relative; padding-left: 27px;
    font-size: 22px; line-height: 35px; font-weight: 400;
  }
  .offer-list li::before {
    content: ""; position: absolute; left: 0; top: 14px;
    width: 9px; height: 9px; border-radius: 50%; background: var(--ink-light);
  }
  .divider-dots {
    position: absolute; left: 0; width: 100%; top: 444px;
    text-align: center; font-size: 20px; letter-spacing: 9px; line-height: 20px;
    padding-left: 9px;
  }
  .owners {
    position: absolute; left: 0; width: 100%; top: 494px;
    text-align: center; font-size: 38px; font-weight: 600; line-height: 52px;
  }
  .contact-list { position: absolute; left: 112px; top: 566px; list-style: none; }
  .contact-list li {
    display: flex; align-items: center; height: 35px;
    font-size: 22px; font-weight: 400;
  }
  .contact-list svg { width: 20px; height: 20px; margin-right: 15px; flex: none; }
  .promo-band {
    position: absolute; left: 0; top: 769px; width: 100%; height: 26px;
    background: linear-gradient(90deg, var(--band-edge), var(--band-mid) 50%, var(--band-edge));
    color: var(--ink-dark); text-align: center;
    font-size: 21px; font-weight: 600; line-height: 27px;
  }
</style>
</head>
<body>
  <section class="card card-front">
    <div class="brand-name">Pine Hollow<br>Makers</div>

    <ul class="offer-list">
      <li>Handmade items</li>
      <li>Handpainted and vinyl signs</li>
      <li>Hoodies</li>
      <li>Wood burned products</li>
      <li>Home decor</li>
    </ul>

    <div class="divider-dots">............</div>

    <div class="owners">Jenna and Brenda</div>

    <ul class="contact-list">
      <li>
        <svg viewBox="0 0 24 24" fill="none" stroke="#fff" stroke-width="2" stroke-linejoin="round"><path d="M5 3h4l2 5-3 2a12 12 0 0 0 6 6l2-3 5 2v4a2 2 0 0 1-2 2A18 18 0 0 1 3 5a2 2 0 0 1 2-2z"/></svg>
        123 123 123
      </li>
      <li>
        <svg viewBox="0 0 24 24" fill="none" stroke="#fff" stroke-width="2" stroke-linejoin="round"><path d="M5 3h4l2 5-3 2a12 12 0 0 0 6 6l2-3 5 2v4a2 2 0 0 1-2 2A18 18 0 0 1 3 5a2 2 0 0 1 2-2z"/></svg>
        123 123 123
      </li>
      <li>
        <svg viewBox="0 0 24 24" fill="none" stroke="#fff" stroke-width="2"><rect x="2" y="5" width="20" height="14"/><path d="M2 5l10 8 10-8M2 19l7-7M22 19l-7-7"/></svg>
        hello@pinehollowmakers.com
      </li>
      <li>
        <svg viewBox="0 0 24 24" fill="none" stroke="#fff" stroke-width="2"><circle cx="12" cy="12" r="10"/><ellipse cx="12" cy="12" rx="4.5" ry="10"/><path d="M2 12h20M4 7h16M4 17h16"/></svg>
        www.pinehollowmakers.com
      </li>
      <li>
        <svg viewBox="0 0 24 24" fill="none" stroke="#fff" stroke-width="2"><circle cx="12" cy="8" r="5"/><path d="M12 13v5M4 21h16"/></svg>
        Home, Street, City, State
      </li>
    </ul>

    <div class="promo-band">Custom work available</div>
  </section>

  <section class="card card-back" role="img" aria-label="Black and white photograph of a tall shingled grain elevator on the left beside old railroad tracks leading to a bridge under a cloudy sky, evergreen trees on the right"></section>
</body>
</html>
```